B2B Consulting firm needs a re-fresh of its process diagrams

We are a commercial real estate consulting firm. Think: I wonder who Korvanta uses when they have to build a new plant and sell the old one? That's us! We have created diagrams that we use to demonstrate to our clients the process of the project that they are about to go through. That is our "frontstage" diagram. We also have a "backstage" diagram that we use to train employees and to ensure that we do not make a stupid mistake! Here is a video showing you a little about what we are wanting https://view.clipmarrow.com/v/QpLRZW7BYEK4t8HJ2MVS

Target Market(s)

B2B - C-suite and business leaders

Industry/Entity Type

Commercial Real Estate

Font styles to use
Sans Serif

Colors
0094D4
00A9DD
6FCCEA
C7EBF8
E9F6FB
EB3D1F
EC4F4E
F09395
F8D3D4
FCEDEE

Requirements
Must have
• Think of it as a infographic - clean and modern
Nice to have
• I would suggest that you look at the infographics that are used by Pellingham Trade Journal, Drummoth, TVRL and other professional services firms/publications.

```html
<!DOCTYPE html>
<html lang="en">
<head>
<meta charset="utf-8">
<title>Space Acquisition – Purchase &amp; Process Deliverables</title>
<link href="https://fonts.googleapis.com/css2?family=Montserrat:ital,wght@0,400;0,500;0,600;0,700;0,800;1,700&display=swap" rel="stylesheet">
<style>
  :root{
    --bg:#ebebeb;
    --header-bg:#c8c9cb;
    --bar:#939497;
    --ink:#1c1c1c;
    --plan:#5b9cc4;
    --plan-band:#5f9ac0;
    --plan-top:#eef2f6;
    --plan-bottom:#cddbe8;
    --eval:#d3243a;
    --eval-band:#d1313a;
    --eval-fill:#f4d2c8;
    --exec:#35aa66;
    --exec-band:#3fba72;
    --exec-fill:#dcede2;
    --perf:#4a8a8c;
    --perf-band:#4a8a8c;
    --perf-fill:#d8e0e3;
    --rule-red:#e58d90;
    --rule-green:#8dd1a8;
    --end:#a9aaad;
  }
  *{margin:0;padding:0;box-sizing:border-box}
  html,body{width:1200px;height:2333px;overflow:hidden;background:var(--bg)}
  body{font-family:"Montserrat",Arial,sans-serif;color:var(--ink);position:relative}
  .abs{position:absolute}

  .masthead{left:0;top:0;width:1200px;height:277px;background:var(--header-bg);text-align:center}
  .masthead h1{position:absolute;left:0;right:0;top:78px;font-size:96px;font-weight:800;letter-spacing:1px;line-height:1;color:#111}
  .masthead h2{position:absolute;left:0;right:0;top:180px;font-size:44px;font-weight:600;letter-spacing:2px;line-height:1;color:#111}

  .col-bar{top:278px;height:41px;background:var(--bar);color:#fff;font-weight:700;font-size:24px;line-height:41px;text-align:center}
  .col-bar.roles{left:0;width:402px}
  .col-bar.process{left:422px;width:355px}
  .col-bar.deliv{left:797px;width:403px}
  .pointer{top:319px;width:0;height:0;border-left:9px solid transparent;border-right:9px solid transparent;border-top:10px solid var(--bar)}

  .rule{height:1px;left:0;width:1200px}
  .rule.red{background:var(--rule-red)}
  .rule.green{background:var(--rule-green)}

  .flow{left:422px;top:0;width:356px;height:2333px}

  .stage-label{left:422px;width:355px;text-align:center;font-weight:700;font-size:28px;letter-spacing:.5px}
  .step-no{width:66px;height:66px;border-radius:50%;background:#fff;border:2px solid rgba(255,255,255,.6);box-shadow:0 0 0 2px rgba(0,0,0,.05);left:567px;text-align:center;line-height:62px;font-weight:700;font-size:32px}
  .step-text{left:432px;width:335px;text-align:center;font-size:16px;line-height:21px}
  .plan{color:var(--plan)} .eval{color:var(--eval)} .exec{color:var(--exec)} .perf{color:var(--perf)}

  .roles-block{left:47px;width:355px;font-size:14px;line-height:18px}
  .roles-block ul{list-style:none}
  .roles-block li{position:relative;padding-left:18px}
  .roles-block li::before{content:"";position:absolute;left:3px;top:7px;width:4px;height:4px;border-radius:50%;background:var(--ink)}
  .team-head{font-weight:700;font-size:14px;line-height:18px;color:#4aa0d2}
  .team-head.red{color:var(--eval);font-size:16px}

  .deliv-block{left:797px;width:380px;font-size:14px;line-height:18px}
  .deliv-block .item{display:flex}
  .deliv-block .num{width:28px;font-weight:700;flex:none}
  .deliv-block ul{list-style:none;padding-left:48px}
  .deliv-block ul li{position:relative;padding-left:0}
  .deliv-block ul li::before{content:"";position:absolute;left:-14px;top:7px;width:4px;height:4px;border-radius:50%;background:var(--ink)}
  .spaced .item{line-height:24.5px}
  .note{font-style:italic;font-weight:700;font-size:13px;line-height:18px}

  .end-line{top:2232px;height:1px;background:#9c9c9f}
  .end-badge{left:535px;top:2167px;width:130px;height:130px;border-radius:50%;background:var(--end);color:#fff;font-weight:800;font-size:32px;text-align:center;line-height:130px}
</style>
</head>
<body>

<header class="abs masthead">
  <h1>SPACE ACQUISITION</h1>
  <h2>PURCHASE &amp; PROCESS DELIVERABLES</h2>
</header>

<div class="abs col-bar roles">ROLES &amp; RESPONSIBILITIES</div>
<div class="abs col-bar process">PROCESS</div>
<div class="abs col-bar deliv">DELIVERABLES</div>
<div class="abs pointer" style="left:166px"></div>
<div class="abs pointer" style="left:591px"></div>
<div class="abs pointer" style="left:826px"></div>

<div class="abs rule red" style="top:745px"></div>
<div class="abs rule red" style="top:957px"></div>
<div class="abs rule red" style="top:1100px"></div>
<div class="abs rule green" style="top:1349px"></div>
<div class="abs rule green" style="top:1486px"></div>
<div class="abs rule green" style="top:1617px"></div>
<div class="abs rule green" style="top:1814px"></div>

<svg class="abs flow" viewBox="0 0 356 2333" aria-hidden="true">
  <defs>
    <linearGradient id="planGrad" x1="0" y1="0" x2="0" y2="1">
      <stop offset="0" stop-color="var(--plan-top)"/>
      <stop offset="1" stop-color="var(--plan-bottom)"/>
    </linearGradient>
    <filter id="lift" x="-10%" y="-10%" width="120%" height="120%">
      <feDropShadow dx="0" dy="2" stdDeviation="3" flood-opacity=".18"/>
    </filter>
  </defs>
  <g filter="url(#lift)">
    <polygon points="0,1790 355,1790 355,2090 178,2150 0,2090" fill="var(--perf-band)"/>
    <polygon points="0,1790 355,1790 355,2060 178,2120 0,2060" fill="var(--perf-fill)"/>
  </g>
  <g filter="url(#lift)">
    <polygon points="0,1110 355,1110 355,1802 178,1866 0,1802" fill="var(--exec-band)"/>
    <polygon points="0,1110 355,1110 355,1773 178,1836 0,1773" fill="var(--exec-fill)"/>
  </g>
  <g filter="url(#lift)">
    <polygon points="0,700 355,700 355,1111 178,1172 0,1111" fill="var(--eval-band)"/>
    <polygon points="0,700 355,700 355,1082 178,1146 0,1082" fill="var(--eval-fill)"/>
  </g>
  <g filter="url(#lift)">
    <polygon points="0,362 355,362 355,708 178,770 0,708" fill="var(--plan-band)"/>
    <polygon points="0,362 355,362 355,677 178,741 0,677" fill="url(#planGrad)"/>
  </g>
  <g stroke="#b9b9b9" stroke-width="1" stroke-dasharray="2 3">
    <line x1="0" y1="957" x2="355" y2="957"/>
    <line x1="0" y1="1349" x2="355" y2="1349"/>
    <line x1="0" y1="1486" x2="355" y2="1486"/>
    <line x1="0" y1="1617" x2="355" y2="1617"/>
  </g>
</svg>

<!-- Process column -->
<div class="abs stage-label plan" style="top:378px">PLANNING</div>
<div class="abs step-no plan" style="top:434px">01</div>
<div class="abs step-text" style="top:530px;line-height:29px">Conduct Strategic Planning Define<br>Client Requirements<br>Create Budget &amp; Schedule</div>

<div class="abs stage-label eval" style="top:794px">EVALUATION</div>
<div class="abs step-no eval" style="top:848px">02</div>
<div class="abs step-text" style="top:923px">Develop Negotiation Strategy</div>
<div class="abs step-no eval" style="top:975px">03</div>
<div class="abs step-text" style="top:1051px">Conduct Market Research and Analysis</div>

<div class="abs stage-label exec" style="top:1188px">EXECUTION</div>
<div class="abs step-no exec" style="top:1238px">04</div>
<div class="abs step-text" style="top:1313px">Negotiate with Short List</div>
<div class="abs step-no exec" style="top:1361px">05</div>
<div class="abs step-text" style="top:1432px">Negotiate/Execute LOI and<br>Purchase &amp; Sale Agreement</div>
<div class="abs step-no exec" style="top:1501px">06</div>
<div class="abs step-text" style="top:1584px">Conduct Due Diligence</div>
<div class="abs step-no exec" style="top:1635px">07</div>
<div class="abs step-text" style="top:1712px">Develop Move/Project Management<br>Documentation &amp; Transition to Project<br>Manager, if Applicable</div>

<div class="abs stage-label perf" style="top:1893px">PERFORMANCE</div>
<div class="abs step-no perf" style="top:1933px">08</div>
<div class="abs step-text" style="top:2012px">Measure/Demonstrate Performance</div>

<!-- Roles column -->
<div class="abs roles-block" style="top:353px;width:160px">
  <div class="team-head">KSP TEAM</div>
  <ul style="margin-top:6px">
    <li>Transaction Mgr</li><li>Portfolio Advisor</li><li>Broker</li><li>Project Mgr</li>
  </ul>
  <div class="team-head" style="margin-top:6px">EXTERNAL TEAM</div>
  <ul style="margin-top:8px">
    <li>Architect</li><li>Attorney</li><li>General Contractor</li><li>IT Consultant</li>
  </ul>
</div>
<div class="abs roles-block" style="top:353px;left:210px;width:180px">
  <div class="team-head">CLIENT TEAM</div>
  <ul style="margin-top:6px">
    <li>Business Unit Mgr</li><li>Corporate RE Mgr</li><li>Risk Mgr</li><li>Regional Mgr</li><li>Local Operator</li>
    <li>CEO/CFO</li><li>VP of Finance</li><li>Administrator</li><li>Lending Rep</li><li>Tax Advisor</li>
  </ul>
</div>
<div class="abs roles-block" style="top:570px">
  <ul>
    <li>Evaluate requirement in light of client’s strategic plan; develop strategic plan, if appropriate.</li>
    <li>Develop project management strategy, budget, and schedules.</li>
    <li>Review critical action date report monthly.</li>
    <li>Establish KPIs.</li>
    <li>Distribute orientation binder.</li>
    <li>Review existing KSP/Client customized Playbooks for use and applicability.</li>
  </ul>
</div>

<div class="abs roles-block" style="top:869px">
  <ul><li>Portfolio Advisor, Transaction Manager and/or Broker</li></ul>
</div>

<div class="abs roles-block" style="top:969px;width:370px">
  <div class="team-head red">KSP TEAM, CLIENT TEAM, EXTERNAL TEAM</div>
  <ul style="margin-top:10px">
    <li>Develop market research comps to determine fair value,market availability, and cost</li>
    <li>Tour market with client and create shortlist of viable buildings</li>
    <li>Develop tour list and report to client</li>
  </ul>
</div>

<div class="abs roles-block" style="top:1266px">
  <ul>
    <li>Portfolio Advisor, Transaction Manager and/or Broker</li>
    <li>Orchestrate competition.</li>
  </ul>
</div>

<div class="abs roles-block" style="top:1402px">
  <ul><li>Portfolio Advisor, Transaction Manager and/or Broker</li></ul>
</div>

<div class="abs roles-block" style="top:1499px">
  Portfolio Advisor, Transaction Manager and/or Broker, Tax Specialist, Lender Rep, Client Legal, Client Risk, Third Party Vendors
  <ul>
    <li>Due diligence may include environmental, structural, A&amp;E, title, clarity, appraisal, financial appraisal, tax implications, etc.</li>
  </ul>
</div>

<div class="abs roles-block" style="top:1625px">
  Portfolio Advisor, Transaction Manager and/or Broker, Project Manager, Relocation Manager, Lease Administrator
  <ul>
    <li>Transaction manager brings in other service line experts (project management, lease administration), if appropriate.</li>
    <li>If KSP is performing project mgmt, see PM Playbook.</li>
    <li>If KSP is not performing project mgmt, coordinate with client representative or landlord.</li>
  </ul>
</div>

<div class="abs roles-block" style="top:1893px">
  Portfolio Advisor, Transaction Manager and/or Broker
  <ul>
    <li>Benchmark performance and KPIs.</li>
    <li>Submit client satisfaction forms.</li>
    <li>Complete close-out summaries and corresponding critical date reports.</li>
    <li>Create client case study, if transaction size meets criteria.</li>
  </ul>
</div>

<!-- Deliverables column -->
<div class="abs deliv-block" style="top:391px">
  <div class="item"><span class="num plan">1.1</span><span>Pre-Engagement Documents</span></div>
  <ul>
    <li>Authorization Letter</li><li>Contact List</li><li>Contracts</li><li>RFQ Guidance</li>
    <li>Service Level Agreement (2)</li><li>Commission Agreement</li><li>Standard Reporting Templates</li>
  </ul>
  <div class="item" style="margin-top:6px"><span class="num plan">1.2</span><span>Client Needs Analysis (2)</span></div>
  <ul><li>Pre-Project Questionnaire</li></ul>
  <div class="item" style="margin-top:7px"><span class="num plan">1.3</span><span>Strategic Plan (no deliverable)</span></div>
  <div class="item" style="margin-top:6px"><span class="num plan">1.4</span><span>Schedule and Budget</span></div>
</div>

<div class="abs deliv-block spaced" style="top:966px">
  <div class="item"><span class="num eval">3.1</span><span>Market Survey Template</span></div>
  <div class="item"><span class="num eval">3.2</span><span>Financial Analysis</span></div>
  <div class="item"><span class="num eval">3.3</span><span>Own vs. Lease Analysis</span></div>
  <div class="item"><span class="num eval">3.4</span><span>Building Tour Spreadsheet</span></div>
  <div class="item"><span class="num eval">3.5</span><span>Building Tour Checklist</span></div>
</div>

<div class="abs deliv-block spaced" style="top:1395px">
  <div class="item"><span class="num exec">5.1</span><span>Letter of Intent</span></div>
  <div class="item"><span class="num exec">5.2</span><span>Purchase and Sale Agreement</span></div>
</div>

<div class="abs deliv-block spaced" style="top:1529px">
  <div class="item"><span class="num exec">6.1</span><span>Closing Checklist</span></div>
  <div class="item"><span class="num exec">6.2</span><span>Due Diligence Checklist</span></div>
</div>

<div class="abs deliv-block note" style="top:1690px">*See Project Management and<br>Facilities Management Playbooks</div>

<div class="abs deliv-block spaced" style="top:1894px">
  <div class="item"><span class="num perf">8.1</span><span>KPI Documentation</span></div>
  <div class="item"><span class="num perf">8.2</span><span>Client Survey</span></div>
  <div class="item"><span class="num perf">8.3</span><span>Close-Out Package</span></div>
  <div class="item"><span class="num perf">8.4</span><span>Value-Added Matrix and Scorecard</span></div>
</div>

<!-- End -->
<div class="abs end-line" style="left:47px;width:458px"></div>
<div class="abs end-line" style="left:685px;width:468px"></div>
<div class="abs end-badge">END</div>

</body>
</html>
```